Web Design Project

We are telecom company based in the Netherlands and we want to create a new design for our company website.

It needs to give a professional, easy to use and clean look.

We currently have an old website. http://www.lumo-tel.com we have started setting up a new site with all the new textual content. We are currently looking for the new look, you can have an idea what we are looking for at the new website location at http://www.lumo-tel.com/nl where the new site is being setup.

We deliver telephone systems and infrastructure like INTERNET and telephone lines. We want to focus on government and cooperate companies.

The logo has the red color that is why we want to use red in the new design.

Target Market(s)

goverment and companies

Industry/Entity Type

Government

```html
<!DOCTYPE html>
<html lang="nl">
<head>
<meta charset="utf-8">
<title>Lumo-Tel – Voordelen van VoIP</title>
<link rel="stylesheet" href="https://fonts.googleapis.com/css2?family=Noto+Sans:wght@400;700&family=Questrial&display=swap">
<style>
  :root {
    --brand-red: #e3141c;
    --bg-red-top: #a10d14;
    --bg-red-bottom: #e21b23;
    --nav-grey: #3d3d3d;
    --text-dark: #1e1e1e;
    --panel-border: #b9b9b9;
    --panel-top: #ffffff;
    --panel-bottom: #e3e3e3;
    --footer-dark: #232122;
    --white: #ffffff;
  }
  * { box-sizing: border-box; margin: 0; padding: 0; }
  html, body { width: 1200px; height: 967px; overflow: hidden; }
  body {
    position: relative;
    font-family: "Noto Sans", Verdana, sans-serif;
    color: var(--text-dark);
    background:
      radial-gradient(ellipse 230px 330px at 70px 800px, rgba(140, 11, 16, 0.55), transparent 70%),
      radial-gradient(ellipse 200px 300px at 1140px 820px, rgba(140, 11, 16, 0.55), transparent 70%),
      linear-gradient(180deg, var(--bg-red-top) 0%, #c4141b 45%, var(--bg-red-bottom) 100%);
  }
  .page {
    position: absolute;
    left: 198px; top: 93px;
    width: 812px; height: 900px;
    background: var(--white);
    border-radius: 8px;
  }
  .brand {
    position: absolute;
    left: 208px; top: 162px;
    width: 128px;
    display: flex; align-items: center; gap: 7px;
  }
  .brand-dot {
    flex: none;
    width: 12px; height: 12px; border-radius: 50%;
    background: var(--brand-red);
  }
  .brand-name {
    font-family: "Questrial", sans-serif;
    font-size: 24px;
    line-height: 1;
    color: var(--brand-red);
    white-space: nowrap;
  }
  .main-nav {
    position: absolute;
    left: 341px; top: 150px;
    width: 646px; height: 58px;
    background: var(--nav-grey);
    border-radius: 0 8px 8px 0;
    display: flex; align-items: center;
    padding-left: 23px; gap: 18.5px;
  }
  .main-nav a {
    font-family: "Questrial", sans-serif;
    font-size: 17.5px;
    color: var(--white);
    text-decoration: none;
  }
  .benefits {
    position: absolute;
    left: 242px; top: 273px;
    width: 370px;
    list-style: none;
    overflow: hidden;
  }
  .benefits li {
    display: flex; align-items: center; gap: 7px;
    height: 24.6px;
    font-size: 14.8px;
    white-space: nowrap;
  }
  .benefits svg { flex: none; }
  .hero-photo {
    position: absolute;
    left: 612px; top: 218px;
    width: 375px; height: 229px;
    border-radius: 0 6px 0 0;
    background: linear-gradient(100deg, #ffffff 0%, #f1f4f7 35%, #dbe3ec 65%, #eef1f5 100%);
  }
  .panel {
    position: absolute;
    top: 476px; height: 400px;
    border: 1px solid var(--panel-border);
    border-radius: 10px;
    background: linear-gradient(180deg, var(--panel-top) 0%, var(--panel-bottom) 100%);
  }
  .panel-voip { left: 216px; width: 499px; padding: 16px 20px 0 30px; overflow: hidden; }
  .panel-contact { left: 729px; width: 262px; padding: 25px 11px 0 11px; }
  .panel-voip h1 {
    font-size: 15.8px; font-weight: 700;
    color: var(--brand-red);
    margin-bottom: 12px;
  }
  .panel-voip h2 {
    font-size: 14px; font-weight: 400;
    color: var(--brand-red);
    margin-bottom: 16px;
  }
  .panel-voip p {
    font-size: 14.1px; line-height: 17.1px;
    margin-bottom: 16px;
  }
  .panel-contact h2 {
    font-size: 15.8px; font-weight: 700;
    color: var(--brand-red);
    padding: 0 0 6px 8px;
    border-bottom: 1px solid var(--panel-border);
  }
  .contact-details {
    font-style: normal;
    font-size: 15.6px; line-height: 19px;
    padding: 10px 0 10px 8px;
    border-bottom: 1px solid var(--panel-border);
  }
  .contact-details p + p { margin-top: 19px; }
  .site-footer {
    position: absolute;
    left: 214px; top: 900px;
    width: 773px; height: 80px;
    background: var(--footer-dark);
    border-radius: 8px 8px 0 0;
    color: var(--white);
    font-size: 15.5px;
    text-align: center;
    padding-top: 25px;
  }
</style>
</head>
<body>
  <div class="page"></div>

  <div class="brand">
    <span class="brand-dot"></span>
    <span class="brand-name">Lumo-Tel</span>
  </div>

  <nav class="main-nav">
    <a href="#">Home</a>
    <a href="#">Lumo-Tel</a>
    <a href="#">Producten</a>
    <a href="#">Diensten</a>
    <a href="#">Reseller</a>
    <a href="#">Support</a>
    <a href="#">Contact</a>
  </nav>

  <ul class="benefits">
    <li><svg width="19" height="18" viewBox="0 0 19 18"><rect x="1" y="3" width="13" height="13" fill="none" stroke="#e3141c" stroke-width="2"/><path d="M4 9l4 4 9-12" fill="none" stroke="#e3141c" stroke-width="2.6"/></svg>gratis bellennaar nevenvestigingen en medewerkers</li>
    <li><svg width="19" height="18" viewBox="0 0 19 18"><rect x="1" y="3" width="13" height="13" fill="none" stroke="#e3141c" stroke-width="2"/><path d="M4 9l4 4 9-12" fill="none" stroke="#e3141c" stroke-width="2.6"/></svg>eenvouding te installeren en beheren</li>
    <li><svg width="19" height="18" viewBox="0 0 19 18"><rect x="1" y="3" width="13" height="13" fill="none" stroke="#e3141c" stroke-width="2"/><path d="M4 9l4 4 9-12" fill="none" stroke="#e3141c" stroke-width="2.6"/></svg>bellen vanuit ow applicaties (bijvoorbeeld outlook)</li>
    <li><svg width="19" height="18" viewBox="0 0 19 18"><rect x="1" y="3" width="13" height="13" fill="none" stroke="#e3141c" stroke-width="2"/><path d="M4 9l4 4 9-12" fill="none" stroke="#e3141c" stroke-width="2.6"/></svg>interactive keuzemenu’s (IVR)</li>
    <li><svg width="19" height="18" viewBox="0 0 19 18"><rect x="1" y="3" width="13" height="13" fill="none" stroke="#e3141c" stroke-width="2"/><path d="M4 9l4 4 9-12" fill="none" stroke="#e3141c" stroke-width="2.6"/></svg>besparing op ow gesprekskosten</li>
  </ul>

  <div class="hero-photo" role="img" aria-label="Foto van een lachende zakenman in een licht overhemd die aan het bellen is"></div>

  <section class="panel panel-voip">
    <h1>Voordelen van VoIP</h1>
    <h2>VoIP en capaciteit</h2>
    <p>Het aantal gesprekken dat tegelijkertijd plaats kan vinden over één VoIP trunk is nagenoeg onbeperkt. Daarmee zal uw teleco-momgeving nooit de beperkende factor zijn bij bedrijfsgroei.</p>
    <h2>VoIP is locatie-onafhankelijk</h2>
    <p>U werkt drie maanden in een ander pand? U gaat verhuizen? Met VoIP geen enkel probleem. Een VoIP account is gekoppeld aan een toestel of aan een VoIP bedrijfscentrale, niet aan een geografische locatie. Dit maakt verhuizen zeer eenvoudig en aanzienlijk voordeliger.</p>
    <h2>VoIP is flexibel</h2>
    <p>U kunt uw telefoontoestel koppelen aan iedere netwerk locatie. Werkt u een periode in een project ruimte, dan neemt u gewoon uw toestel mee. Er hoeft niets omgeschakeld te</p>
  </section>

  <aside class="panel panel-contact">
    <h2>Lumo-Tel</h2>
    <address class="contact-details">
      <p>Veldhovenstraat 48<br>1071 KP Amsterdam<br>The Netherlands</p>
      <p>Telefoon nr. :<br>+31 (0) 20 5 550 142</p>
      <p>Fax nr. :<br>&nbsp;+31 (0) 20 5 550 143</p>
      <p>Email :<br>&nbsp;info@Lumo-Tel.com</p>
    </address>
  </aside>

  <footer class="site-footer">2012 Norvalt Telecom BV. Alle rechten voorbehouden.</footer>
</body>
</html>
```